Website for designing and selling name-labels

We are looking for a fresh design for a site similar to these (www.merkefin.no, www.tagglykke.no, www.skogtrykk.no) where the consumer can come online designing their own labels (30x15 mm) , either with onlye text or with text, choose a pre-defined symbol (which we have) and/or a color. We will the print the labels on our side, and send it to the customer.

We are looking for the front page, product page and check out - page.

Target Market(s)

families with childring, scools, kinder garden, industry

Number of Pages Required

3 page

Requirements
Nice to have
• bright and easy design
easy to design and see their own designs
easy check out - few steps

```html
<!DOCTYPE html>
<html lang="en">
<head>
<meta charset="utf-8">
<title>Lappestua.no – Design your own name tags</title>
<link href="https://fonts.googleapis.com/css2?family=Roboto:ital,wght@0,400;0,500;0,700;1,400&display=swap" rel="stylesheet">
<style>
:root{
  --teal:#17a398;
  --teal-dark:#128c83;
  --mint:#c4fbf8;
  --ink:#111;
  --text:#333;
  --muted:#555;
  --panel:#f4f4f4;
  --line:#e3e3e3;
  --hero-a:#c7d8e6;
  --hero-b:#a9c2d6;
}
*{box-sizing:border-box;margin:0;padding:0}
html,body{width:1200px;height:2945px;overflow:hidden;background:#fff}
body{font-family:"Roboto",Arial,sans-serif;color:var(--text);position:relative}
.abs{position:absolute}

/* header */
.logo{left:100px;top:8px;width:168px;height:46px;background:var(--teal);border-radius:4px;color:#fff;display:flex;align-items:center;justify-content:center;font-weight:700;font-size:15px;letter-spacing:.3px}
.nav{left:327px;top:22px;display:flex;gap:28px;font-size:14px;color:#222}
.cart{left:1070px;top:14px}
.trust{top:80px;display:flex;gap:10px;align-items:center}
.trust h4{font-size:16px;font-weight:700;color:#111;text-transform:uppercase}
.trust p{font-size:14px;color:#555;margin-top:4px}

/* hero */
.hero{left:100px;top:145px;width:1000px;height:469px;background:linear-gradient(90deg,var(--hero-a),var(--hero-b))}
.hero-photo{position:absolute;left:410px;top:0;width:590px;height:469px;background:radial-gradient(ellipse at 45% 55%,#f3f3f0 0%,#dfe4e8 38%,rgba(169,194,214,0) 70%)}
.hero h1{position:absolute;left:83px;top:162px;color:#fff;font-size:32px;font-weight:700}
.hero .sub{position:absolute;left:83px;top:213px;color:#fff;font-size:20px}
.btn{background:var(--teal);color:#fff;font-weight:500;text-transform:uppercase;display:flex;align-items:center;justify-content:center;border-radius:2px}
.hero .btn{position:absolute;left:84px;top:256px;width:157px;height:44px;font-size:16px}
.dots{position:absolute;left:462px;top:428px;display:flex;gap:9px}
.dots i{width:12px;height:12px;border:1.5px solid #fff;border-radius:50%}
.dots i.on{background:#fff}

/* sections */
.title{width:1200px;left:0;text-align:center;font-size:35px;font-weight:700;color:#111;text-transform:uppercase}
.subtitle{width:1200px;left:0;text-align:center;font-size:18px;color:#222}
.tile{text-align:center}
.tile .img{border-radius:18px}
.tile h3{font-size:18px;font-weight:500;color:#111;margin-top:14px}
.tile p{font-size:12.5px;color:#444;margin-top:6px}
.wide .img{border-radius:0;height:339px}

/* label designer */
.designer{left:100px;top:1577px;width:1000px;height:448px;background:var(--panel)}
.designer h2{position:absolute;left:520px;top:64px;font-size:26px;font-weight:700;color:#111;line-height:37px}
.designer .desc{position:absolute;left:521px;top:141px;width:450px;font-size:14.5px;line-height:24px;color:#444}
.lbl{position:absolute;font-size:15px;color:#333}
.input{position:absolute;left:522px;top:273px;width:198px;height:37px;background:#fff;border:1px solid var(--line)}
.sym{position:absolute;left:742px;top:274px;display:flex;align-items:center;gap:10px}
.sym b{width:32px;height:32px;border-radius:50%;background:#fff;border:1px solid var(--line);display:block}
.sym b.dk{background:#cfcfcf}
.colors{position:absolute;left:523px;top:356px;display:flex;gap:6px}
.colors i{width:22px;height:22px;border-radius:50%}
.designer .btn{position:absolute;left:741px;top:333px;width:156px;height:43px;font-size:16px}

/* feedback */
.review{top:2154px;width:321px;height:209px;background:#fff;box-shadow:0 0 12px rgba(0,0,0,.08);text-align:center;padding:24px 18px}
.review p{font-style:italic;font-size:12px;line-height:20.5px;color:#333}
.who{display:flex;justify-content:center;align-items:center;gap:8px;margin-top:8px}
.who .av{width:40px;height:40px;border-radius:50%;background:linear-gradient(#bfc9d2,#7f8d99)}
.who div{text-align:left;font-size:14px;color:#111;line-height:15px}
.stars{color:#f5b800;font-size:11px;letter-spacing:1px}

/* footer */
.foot{left:0;top:2418px;width:1200px;height:309px;background:var(--mint)}
.foot h4{position:absolute;top:66px;font-size:16px;font-weight:700;color:#111}
.foot .item{position:absolute;font-size:15px;color:#333;display:flex;gap:8px;align-items:flex-start;line-height:20px}
.email{position:absolute;left:277px;top:94px;width:316px;height:40px;background:#fff;border-radius:20px;padding-left:16px;display:flex;align-items:center;font-size:14px;color:#333}
.email .go{position:absolute;right:3px;top:3px;width:58px;height:34px;border-radius:17px;background:var(--teal);display:flex;align-items:center;justify-content:center}
.base{left:0;top:2727px;width:1200px;height:218px;background:var(--teal);color:#fff}
.pay{position:absolute;top:58px;left:0;width:1200px;display:flex;justify-content:center;align-items:center;gap:30px;font-weight:700;font-size:22px}
.pay .ring{width:26px;height:26px;border-radius:50%;background:#fff;display:inline-block;vertical-align:middle;margin-right:6px}
.copy{position:absolute;top:126px;width:1200px;text-align:center;font-size:12.5px}
.social{position:absolute;top:174px;left:560px;display:flex;gap:14px}
.social i{width:18px;height:18px;border-radius:50%;background:#fff;display:block}
</style>
</head>
<body>

<header>
  <div class="abs logo">LAPPESTUA.NO</div>
  <nav class="abs nav">
    <span>Name tags</span><span>Minilapper</span><span>Large name tags</span><span>Famous characters</span><span>Wall decoration</span><span>Blog</span><span>Other &#x2304;</span>
  </nav>
  <svg class="abs cart" width="30" height="32" viewBox="0 0 30 32" aria-label="Cart">
    <path d="M4 10h18l1 18H3z" fill="none" stroke="#333" stroke-width="1.8"/>
    <path d="M8 10V7a5 5 0 0 1 10 0v3" fill="none" stroke="#333" stroke-width="1.8"/>
    <circle cx="22" cy="24" r="7" fill="var(--teal)"/>
    <text x="22" y="28" fill="#fff" font-size="10" text-anchor="middle" font-family="Roboto,sans-serif">0</text>
  </svg>

  <div class="abs trust" style="left:100px">
    <svg width="47" height="47" viewBox="0 0 47 47"><circle cx="23.5" cy="23.5" r="21" fill="none" stroke="var(--teal)" stroke-width="5"/></svg>
    <div><h4>Over 200,000 satisfied customers</h4><p>Since 2020</p></div>
  </div>
  <div class="abs trust" style="left:532px">
    <svg width="66" height="44" viewBox="0 0 66 44"><rect x="2" y="6" width="38" height="26" rx="2" fill="var(--teal)"/><path d="M40 14h14l10 10v8H40z" fill="var(--teal)"/><circle cx="14" cy="36" r="6" fill="var(--teal)" stroke="#fff" stroke-width="2"/><circle cx="52" cy="36" r="6" fill="var(--teal)" stroke="#fff" stroke-width="2"/></svg>
    <div><h4>Free shipping</h4><p>2-3 days delivery time</p></div>
  </div>
  <div class="abs trust" style="left:828px">
    <svg width="48" height="48" viewBox="0 0 48 48"><circle cx="24" cy="20" r="18" fill="var(--teal)"/><path d="M15 20l6 6 12-12" fill="none" stroke="#fff" stroke-width="4"/><path d="M12 34l-6 10 8-2 4 6 4-10M36 34l6 10-8-2-4 6-4-10" fill="var(--teal)"/></svg>
    <div><h4>Satisfaction guarantee</h4><p>100% satisfied or money back</p></div>
  </div>
</header>

<section class="abs hero">
  <div class="hero-photo" role="img" aria-label="Flat lay of white baby romper, knitted shoes, teething toys and a blue bib on a pale blue background"></div>
  <h1>DESIGN YOUR OWN TAGS</h1>
  <div class="sub">Design Your Own Tags</div>
  <div class="btn">Make now</div>
  <svg style="position:absolute;left:20px;top:220px" width="18" height="32"><path d="M16 2L3 16l13 14" fill="none" stroke="#fff" stroke-width="2"/></svg>
  <svg style="position:absolute;left:960px;top:220px" width="18" height="32"><path d="M2 2l13 14L2 30" fill="none" stroke="#fff" stroke-width="2"/></svg>
  <div class="dots"><i class="on"></i><i></i><i></i><i></i></div>
</section>

<h2 class="abs title" style="top:698px">Find your favorite!</h2>
<div class="abs subtitle" style="top:743px">Design Your Own Tags</div>

<div class="abs tile" style="left:100px;top:789px;width:239px">
  <div class="img" style="height:232px;background:linear-gradient(135deg,#b8ddd6,#c99a63 55%,#5b3a26)" role="img" aria-label="Name tag sewn into a brown knitted sweater beside a toy block"></div>
  <h3>Name tags</h3><p>For clothes and equipment</p>
</div>
<div class="abs tile" style="left:354px;top:789px;width:239px">
  <div class="img" style="height:232px;background:linear-gradient(135deg,#bfeee3,#a6e3d6 60%,#8ed4c6)" role="img" aria-label="Sheet of name patches with a water bottle and toys on mint green"></div>
  <h3>Large patches</h3><p>For clothes and equipment</p>
</div>
<div class="abs tile" style="left:607px;top:789px;width:239px">
  <div class="img" style="height:232px;background:linear-gradient(135deg,#d3f3e1,#eef9f2 55%,#bfe9cf)" role="img" aria-label="Sheets of small green name stickers with a toy"></div>
  <h3>Minilapper</h3><p>For clothes and equipment</p>
</div>
<div class="abs tile" style="left:861px;top:789px;width:239px">
  <div class="img" style="height:232px;background:linear-gradient(180deg,#f6f6f4,#e9e6df 60%,#b7c4b3)" role="img" aria-label="Children's wall stickers above baskets of soft toys"></div>
  <h3>Wall decoration</h3><p>Create magical children's rooms</p>
</div>

<div class="abs tile wide" style="left:100px;top:1107px;width:489px">
  <div class="img" style="background:linear-gradient(135deg,#f2f0ee,#e8e5e1 60%,#c9c3bb)" role="img" aria-label="Children's room with star wall stickers, a teddy bear on a chair and a play tent"></div>
  <h3>Wall stickers for children's rooms</h3><p>Create magical children's rooms with our brand new wall stickers!</p>
</div>
<div class="abs tile wide" style="left:611px;top:1107px;width:489px">
  <div class="img" style="background:linear-gradient(135deg,#f4f5f3,#e9ecea 55%,#c6d6e2)" role="img" aria-label="Iron pressing a name label onto a white baby garment"></div>
  <h3>Ironing pads</h3><p>For all types of clothing</p>
</div>

<section class="abs designer">
  <div style="position:absolute;left:25px;top:25px;width:450px;height:398px;background:linear-gradient(135deg,#3b8fb6,#5aa7cb 50%,#e8eef2)" role="img" aria-label="Baby hat, white shorts with name label and a blue bunny comforter on a blue background"></div>
  <h2>DESIGN YOUR NAME-LABELS<br>(30X15 MM)</h2>
  <p class="desc">Lorem ipsum dolor sit amet, consectetur adipiscing elit, sed do eiusmod tempor incididunt ut labore et dologna aliqua. Quis ipsum suspendisse ultrices gravida. Risus commodo viverra maecenas accumsan lacus vel facilisis.</p>
  <div class="lbl" style="left:522px;top:249px">Enter The Text</div>
  <div class="input"></div>
  <div class="lbl" style="left:746px;top:249px">Choose a pre-defined symbol</div>
  <div class="sym">
    <svg width="10" height="14"><path d="M8 1L2 7l6 6" fill="none" stroke="#555" stroke-width="1.5"/></svg>
    <b></b><b></b><b></b><b class="dk"></b>
    <svg width="10" height="14"><path d="M2 1l6 6-6 6" fill="none" stroke="#555" stroke-width="1.5"/></svg>
  </div>
  <div class="lbl" style="left:520px;top:328px">Choose a Color</div>
  <div class="colors">
    <i style="background:#8a10d0"></i><i style="background:#4b0a8c"></i><i style="background:#1414e8"></i><i style="background:#12e012"></i><i style="background:#f27d0c"></i><i style="background:#f01010"></i>
  </div>
  <div class="btn">Print now</div>
</section>

<h2 class="abs title" style="top:2098px">Customer feedback</h2>

<div class="abs review" style="left:100px">
  <p>Lorem ipsum dolor sit amet, consectetur adipiscing elit, sed do eiusmod tempor incididunt ut labore et dolore magna aliqua. Quis ipsum pendisse ultrices gravida. Risus commodo viverra maecenas accumsan lacus vel facilisis.</p>
  <div class="who"><span class="av"></span><div>John Doe<br><span class="stars">★★★★★</span></div></div>
</div>
<div class="abs review" style="left:439px">
  <p>Lorem ipsum dolor sit amet, consectetur adipiscing elit, sed do eiusmod tempor incididunt ut labore et dolore magna aliqua. Quis ipsum pendisse ultrices gravida. Risus commodo viverra maecenas accumsan lacus vel facilisis.</p>
  <div class="who"><span class="av"></span><div>John Doe<br><span class="stars">★★★★★</span></div></div>
</div>
<div class="abs review" style="left:779px">
  <p>Lorem ipsum dolor sit amet, consectetur adipiscing elit, sed do eiusmod tempor incididunt ut labore et dolore magna aliqua. Quis ipsum pendisse ultrices gravida. Risus commodo viverra maecenas accumsan lacus vel facilisis.</p>
  <div class="who"><span class="av"></span><div>John Doe<br><span class="stars">★★★★★</span></div></div>
</div>

<footer>
  <div class="abs foot">
    <h4 style="left:100px">CONTACT US</h4>
    <div class="item" style="left:100px;top:98px">
      <svg width="16" height="14"><rect x="1" y="2" width="14" height="10" fill="none" stroke="#333" stroke-width="1.3"/><path d="M1 2l7 6 7-6" fill="none" stroke="#333" stroke-width="1.3"/></svg>info@lappestua.no</div>
    <div class="item" style="left:100px;top:130px">
      <svg width="14" height="16"><path d="M3 1l3 3-2 3c1 2 3 4 5 5l3-2 3 3-2 2C7 15 0 8 1 3z" fill="#333"/></svg>888 888 8888</div>
    <div class="item" style="left:100px;top:162px">
      <svg width="10" height="14"><path d="M5 14C1 8 0 6 0 5a5 5 0 0 1 10 0c0 1-1 3-5 9z" fill="#333"/><circle cx="5" cy="5" r="2" fill="var(--mint)"/></svg>1234 Somestreet Anywhere<br>USA 21212</div>

    <h4 style="left:384px">RECEIVE OFFERS AND INFO BY E-MAIL</h4>
    <div class="email" style="left:377px">Email
      <span class="go"><svg width="26" height="12"><path d="M1 6h23M18 1l6 5-6 5" fill="none" stroke="#fff" stroke-width="1.5"/></svg></span>
    </div>

    <h4 style="left:760px">FIND OUT MORE</h4>
    <div class="item" style="left:760px;top:98px">Contact Us</div>
    <div class="item" style="left:760px;top:130px">100% satisfaction guarantee</div>
    <div class="item" style="left:760px;top:162px">Kindergarten materials</div>
    <div class="item" style="left:760px;top:194px">Materials for old people's homes &amp;nursing homes</div>
    <div class="item" style="left:760px;top:226px">Vacancy</div>
  </div>

  <div class="abs base">
    <div class="pay">
      <span>Bankly</span><span>Kortpay</span><span><span class="ring"></span>Sirkelkort</span><span>Mobilo</span>
    </div>
    <div class="copy">© 2021 Lappestua. All Rights Reserved &nbsp; | &nbsp; Contact us &nbsp; | &nbsp; Terms Privacy</div>
    <div class="social"><i aria-label="Social link one"></i><i aria-label="Social link two"></i><i aria-label="Social link three"></i></div>
  </div>
</footer>

</body>
</html>
```